Real estate development company, seeking investors and joint venture partners to fund

i have attached a investor proposal document to attact joint venture money partners to invest in property development. the existing document i have attached need s to be polised to a professional standard and needs to be in word , so i can edit the content on ongoing basis i.e. numbers and photos etc . this document will be updated with new opportunites, propoerties, feasibility edited and emailed to potential investors. This document needs to be Red hot!! Company name Bright meadow collective. All tables, place holders for photos need to be provided so i can easily remove and paste new /updated photos.

Target Market(s)

investors , money partners property developers

Requirements
Must have
• Design to be in word document

Content should be modifyable by me as each project will have unique cost, sales etc

i want to be able to email to my clients

i may also print as required
Nice to have
• Feel free to modify table/images/look and feel

```html
<!DOCTYPE html>
<html lang="en">
<head>
<meta charset="utf-8">
<title>Investor Report – Bright Meadow Collective</title>
<link rel="stylesheet" href="https://fonts.googleapis.com/css2?family=Archivo+Black&family=Roboto:wght@400;500;700&display=swap">
<style>
:root{
  --backdrop:#a6a6a6;
  --cream:#fdf2b8;
  --cream-light:#fef8d6;
  --gold:#f5c540;
  --gold-deep:#efb21f;
  --navy:#26286b;
  --ink:#4a4a4a;
  --grey-bar:#ececec;
  --white:#ffffff;
  --photo-warm:#d9a98a;
  --photo-red:#b8323a;
  --photo-grey:#8e8f94;
  --photo-green:#8fbf52;
}
*{box-sizing:border-box;margin:0;padding:0}
html,body{width:1200px;height:2769px;overflow:hidden}
body{background:var(--backdrop);font-family:"Roboto",Arial,sans-serif;color:var(--ink);position:relative}

.page{position:absolute;width:522px;height:735px;background:var(--white);overflow:hidden;box-shadow:0 4px 12px rgba(0,0,0,.25)}
.page::before{content:"";position:absolute;left:0;top:0;right:0;height:5px;background:var(--gold)}

/* Cover */
.cover{width:564px;height:797px;background:linear-gradient(180deg,var(--cream) 0%,var(--cream-light) 100%);transform-origin:top left}
.cover::after{content:"";position:absolute;left:0;bottom:0;right:0;height:5px;background:var(--gold)}
.cover-header{position:absolute;left:24px;top:8px;width:516px;height:116px;background:var(--white)}
.contact-line{position:absolute;left:14px;display:flex;align-items:center;gap:9px;font-size:15px;color:var(--ink)}
.contact-line svg{width:20px;height:20px}
.brand{position:absolute;left:318px;top:22px;display:flex;align-items:center;gap:12px}
.brand-square{width:62px;height:62px;background:var(--gold)}
.brand-name{font-family:"Roboto",Arial,sans-serif;font-weight:700;font-size:19px;line-height:1.1;color:#555}
.cover-title{position:absolute;left:30px;top:168px;font-family:"Archivo Black",Arial,sans-serif;color:var(--gold);-webkit-text-stroke:1.5px #b88a1a;line-height:.98}
.cover-title .l1{display:block;font-size:50px;letter-spacing:.5px}
.cover-title .l2{display:block;font-size:64px}
.cover-sub{position:absolute;left:31px;top:302px;font-size:22px;font-weight:500;color:var(--navy)}
.cover-art{position:absolute;left:0;top:0}
.prepared{position:absolute;left:0;right:0;top:675px;text-align:center;font-size:16px;color:var(--ink);line-height:1.4}
.prepared .who{display:block;font-weight:700;font-size:21px;color:var(--gold-deep)}
.prepared .org,.prepared .abn{display:block;font-size:15px;color:var(--navy)}

/* Inner page chrome */
.page-head{position:absolute;left:0;top:8px;width:100%;height:26px;background:var(--grey-bar)}
.call{position:absolute;left:32px;top:5px;font-size:12px;letter-spacing:1.3px;color:#555;display:flex;align-items:center;gap:6px}
.call svg{width:15px;height:15px}
.head-brand{position:absolute;right:0;top:0;width:178px;height:26px;background:var(--navy);color:var(--white);font-size:12px;display:flex;align-items:center;justify-content:center}
.page-foot{position:absolute;left:0;bottom:0;width:100%;height:78px;background:linear-gradient(180deg,#fbe4d3 0%,#f9dcc6 55%,#8fd2e4 80%,#6fc3da 100%)}
.page-no{position:absolute;right:22px;bottom:16px;width:16px;height:16px;border-radius:50%;background:var(--navy);color:var(--white);font-size:9px;display:flex;align-items:center;justify-content:center}
.photo{position:absolute}

.body-copy{position:absolute;left:34px;width:454px;font-size:10.5px;line-height:1.42;text-align:justify;color:#555}
.body-copy p{margin-bottom:14px}
.signature{position:absolute;left:34px;top:362px;width:120px;border-top:1px dashed #777;font-size:10px;color:#555;text-align:center;padding-top:4px;line-height:1.45}

.contents-panel{position:absolute;left:34px;top:73px;width:454px;height:615px;background:var(--cream)}
.section-title{font-family:"Archivo Black",Arial,sans-serif;color:var(--gold);-webkit-text-stroke:1px #b88a1a;text-align:center}
.contents-panel .section-title{margin-top:16px;font-size:36px}
.rule{width:128px;height:3px;background:var(--navy);margin:4px auto 0}
.toc{list-style:none;margin-top:22px;text-align:center;font-size:12px;color:#555}
.toc li{height:41.3px}

.proposal-title{position:absolute;left:0;right:0;top:72px}
.proposal-title .section-title{font-size:28px}
.sub-head{position:absolute;left:34px;font-size:16px;font-weight:700;color:var(--navy)}
.outcomes{position:absolute;left:34px;top:297px;width:454px;border-collapse:separate;border-spacing:0 1px;font-size:10px}
.outcomes td{height:20px;padding-left:46px}
.outcomes .label{background:#efefef;color:#555;width:226px}
.outcomes .value{background:var(--navy);color:var(--white)}
</style>
</head>
<body>

<!-- Cover, top -->
<section class="page cover" style="left:327px;top:178px">
  <svg class="cover-art" width="564" height="797" viewBox="0 0 564 797">
    <defs>
      <linearGradient id="gMain" x1="0" y1="0" x2="1" y2="1"><stop offset="0" stop-color="#f3e4cf"/><stop offset=".6" stop-color="#d9a98a"/><stop offset="1" stop-color="#9a6a55"/></linearGradient>
      <linearGradient id="gTop" x1="0" y1="0" x2="1" y2="1"><stop offset="0" stop-color="#c58b6f"/><stop offset="1" stop-color="#b8323a"/></linearGradient>
      <linearGradient id="gBot" x1="0" y1="0" x2="1" y2="1"><stop offset="0" stop-color="#6d6e73"/><stop offset="1" stop-color="#c7c8cc"/></linearGradient>
    </defs>
    <polygon points="0,358 300,358 395,478 325,657 0,657" fill="url(#gMain)" role="img" aria-label="Photo: mother helping children draw at a table"/>
    <polygon points="440,212 564,212 564,462 410,462 325,345" fill="url(#gTop)" role="img" aria-label="Photo: children playing on a red play mat"/>
    <polygon points="425,480 564,480 564,657 345,657" fill="url(#gBot)" role="img" aria-label="Photo: boy with headphones at a desk"/>
    <line x1="452" y1="158" x2="340" y2="297" stroke="#26286b" stroke-width="2"/>
    <line x1="430" y1="205" x2="333" y2="308" stroke="#26286b" stroke-width="2"/>
    <line x1="375" y1="490" x2="327" y2="560" stroke="#fff" stroke-width="1.5"/>
  </svg>
  <div class="cover-header">
    <div class="contact-line" style="top:34px"><svg viewBox="0 0 20 20"><circle cx="10" cy="10" r="10" fill="#f5c540"/><rect x="7" y="4.5" width="6" height="11" rx="1" fill="none" stroke="#fff" stroke-width="1.4"/></svg>0400-555-018</div>
    <div class="contact-line" style="top:66px"><svg viewBox="0 0 20 20"><circle cx="10" cy="10" r="10" fill="#f5c540"/><rect x="5" y="6.5" width="10" height="7" fill="none" stroke="#fff" stroke-width="1.3"/><path d="M5 6.5l5 4 5-4" fill="none" stroke="#fff" stroke-width="1.3"/></svg>info@brightmeadow.example</div>
    <div class="brand"><span class="brand-square"></span><span class="brand-name">Bright<br>Meadow<br>Collective</span></div>
  </div>
  <h1 class="cover-title"><span class="l1">INVESTOR</span><span class="l2">REPORT</span></h1>
  <div class="cover-sub">DUAL OCC DEVELOPMENT</div>
  <div class="prepared">Prepared By<span class="who">DANIEL OKAFOR</span><span class="org">Bright Meadow Collective</span><span class="abn">ABN</span></div>
</section>

<!-- Cover, in spread -->
<section class="page cover" style="left:62px;top:1195px;transform:scale(.924)">
  <svg class="cover-art" width="564" height="797" viewBox="0 0 564 797">
    <polygon points="0,358 300,358 395,478 325,657 0,657" fill="url(#gMain)" role="img" aria-label="Photo: mother helping children draw at a table"/>
    <polygon points="440,212 564,212 564,462 410,462 325,345" fill="url(#gTop)" role="img" aria-label="Photo: children playing on a red play mat"/>
    <polygon points="425,480 564,480 564,657 345,657" fill="url(#gBot)" role="img" aria-label="Photo: boy with headphones at a desk"/>
    <line x1="452" y1="158" x2="340" y2="297" stroke="#26286b" stroke-width="2"/>
    <line x1="430" y1="205" x2="333" y2="308" stroke="#26286b" stroke-width="2"/>
    <line x1="375" y1="490" x2="327" y2="560" stroke="#fff" stroke-width="1.5"/>
  </svg>
  <div class="cover-header">
    <div class="contact-line" style="top:34px"><svg viewBox="0 0 20 20"><circle cx="10" cy="10" r="10" fill="#f5c540"/><rect x="7" y="4.5" width="6" height="11" rx="1" fill="none" stroke="#fff" stroke-width="1.4"/></svg>0400-555-018</div>
    <div class="contact-line" style="top:66px"><svg viewBox="0 0 20 20"><circle cx="10" cy="10" r="10" fill="#f5c540"/><rect x="5" y="6.5" width="10" height="7" fill="none" stroke="#fff" stroke-width="1.3"/><path d="M5 6.5l5 4 5-4" fill="none" stroke="#fff" stroke-width="1.3"/></svg>info@brightmeadow.example</div>
    <div class="brand"><span class="brand-square"></span><span class="brand-name">Bright<br>Meadow<br>Collective</span></div>
  </div>
  <h1 class="cover-title"><span class="l1">INVESTOR</span><span class="l2">REPORT</span></h1>
  <div class="cover-sub">DUAL OCC DEVELOPMENT</div>
  <div class="prepared">Prepared By<span class="who">DANIEL OKAFOR</span><span class="org">Bright Meadow Collective</span><span class="abn">ABN</span></div>
</section>

<!-- Page 2: introduction letter -->
<section class="page" style="left:610px;top:1195px">
  <div class="page-head"><span class="call"><svg viewBox="0 0 16 16"><circle cx="8" cy="8" r="8" fill="#555"/><rect x="5.5" y="3.5" width="5" height="9" rx="1" fill="none" stroke="#fff" stroke-width="1.2"/></svg>Call Us Now : 0400-555-018</span><span class="head-brand">Bright Meadow Collective</span></div>
  <div class="body-copy" style="top:82px">
    <p>Lorem Ipsum is simply dummy text of the printing and typesetting industry. Lorem Ipsum has been the industry's standard dummy text ever since the 1500s, when an unknown printer took a galley of type and scrambled it to make a type specimen book. It has survived not only five centuries, but also the leap into electronic typesetting, remaining essentially unchanged. It was popularised in the 1960s with the release of transfer sheets containing Lorem Ipsum passages, and more recently with desktop publishing tools and layout software including versions of Lorem Ipsum.</p>
    <p>Lorem Ipsum is simply dummy text of the printing and typesetting industry. Lorem Ipsum has been the industry's standard dummy text ever since the 1500s, when an unknown printer took a galley of type and scrambled it to make a type specimen book.</p>
    <p>It has survived not only five centuries, but also the leap into electronic typesetting, remaining essentially unchanged. It was popularised in the 1960s with the release of transfer sheets containing Lorem Ipsum passages, and more recently with desktop publishing tools and layout software including versions of Lorem Ipsum.</p>
  </div>
  <div class="signature">Signature<br>( Name Goes Here)</div>
  <div class="page-foot" role="img" aria-label="Playful underwater border illustration"></div>
  <div class="photo" style="left:34px;top:428px;width:454px;height:255px;background:linear-gradient(180deg,#d8cfc2 0%,#b59b86 50%,#8fbf52 80%,#6aa43a 100%)" role="img" aria-label="Photo: children drawing together on the grass"></div>
  <span class="page-no">2</span>
</section>

<!-- Page 3: contents -->
<section class="page" style="left:62px;top:1962px">
  <div class="page-head"><span class="call"><svg viewBox="0 0 16 16"><circle cx="8" cy="8" r="8" fill="#555"/><rect x="5.5" y="3.5" width="5" height="9" rx="1" fill="none" stroke="#fff" stroke-width="1.2"/></svg>Call Us Now : 0400-555-018</span><span class="head-brand">Bright Meadow Collective</span></div>
  <div class="page-foot" role="img" aria-label="Playful underwater border illustration"></div>
  <div class="contents-panel">
    <h2 class="section-title">CONTENTS</h2>
    <div class="rule"></div>
    <ul class="toc">
      <li>PROPOSAL &nbsp;|&nbsp; 4</li>
      <li>LOCATION &nbsp;|&nbsp; 4</li>
      <li>PHOTOS &nbsp;|&nbsp; 5</li>
      <li>FINANCIAL FEASIBILITY &nbsp;|&nbsp; 5</li>
      <li>CASH FLOW ANALYSIS &nbsp;|&nbsp; 6</li>
      <li>CAPITAL REQUIREMENTS &nbsp;|&nbsp; 7</li>
      <li>SUBURB PROFILE &nbsp;|&nbsp; 8</li>
      <li>COMPARABLE SALES DATA &nbsp;|&nbsp; 10</li>
      <li>PLANNING INFORMATION &nbsp;|&nbsp; 13</li>
      <li>TESTIMONIALS &nbsp;|&nbsp; 16</li>
      <li>WHO ARE YOU? &nbsp;|&nbsp; 16</li>
      <li>CONTACT &nbsp;|&nbsp; 20</li>
    </ul>
  </div>
  <span class="page-no">3</span>
</section>

<!-- Page 4: proposal -->
<section class="page" style="left:613px;top:1962px">
  <div class="page-head"><span class="call"><svg viewBox="0 0 16 16"><circle cx="8" cy="8" r="8" fill="#555"/><rect x="5.5" y="3.5" width="5" height="9" rx="1" fill="none" stroke="#fff" stroke-width="1.2"/></svg>Call Us Now : 0400-555-018</span><span class="head-brand">Bright Meadow Collective</span></div>
  <div class="proposal-title"><h2 class="section-title">PROPOSAL</h2><div class="rule"></div></div>
  <h3 class="sub-head" style="top:160px">PROJECT GOAL</h3>
  <div class="body-copy" style="top:194px;text-align:left">Purchase an existing house on a block of land, obtain development approval to demolish existing house and build two townhouses (dual occupancy side by side)</div>
  <h3 class="sub-head" style="top:264px">PROJECT OUTCOMES</h3>
  <table class="outcomes">
    <tr><td class="label">Project Type</td><td class="value">2 Townhouse Development</td></tr>
    <tr><td class="label">Total Project Costs</td><td class="value">$1,900,000</td></tr>
    <tr><td class="label">Total Cash/Equity Required</td><td class="value">$627,991</td></tr>
    <tr><td class="label">Indicative Project Net Profit</td><td class="value">$250,093</td></tr>
    <tr><td class="label">Indicative Project Return</td><td class="value">40%</td></tr>
  </table>
  <div class="page-foot" role="img" aria-label="Playful underwater border illustration"></div>
  <div class="photo" style="left:34px;top:428px;width:454px;height:255px;background:linear-gradient(135deg,#b0444a 0%,#5a3a3a 40%,#2c2b33 75%,#8a2e35 100%)" role="img" aria-label="Photo: school children in blazers seated in a classroom"></div>
  <span class="page-no">4</span>
</section>

</body>
</html>
```